Powerpoint template for our Credentials presentation for our new consulting business - Channel Spen

We are a new company called Channel Spend Clearview (CSC) based in Sydney Australia

We have both run media buying agencies for many years.

Those agencies run by multi-national organisations are becoming less and less transparent with the transactions that they are managing – clients are being significantly over-charged in many areas – especially digital media.

At the same time, our experience has told us that most clients have little understanding of how media should be planned and bought

We are making ourselves available to those clients who cant afford a full time specialist but want to ensure that they are making the correct media and marketing decisions that benefit them rather than their agency.

Target Market(s)

Marketing Managers and Directors

Industry/Entity Type

Media

Other font styles liked:
• Font used in our logo (attached)

Colors
33a6d7
fbee3e
ffffff

Requirements
Must have
• We have provided the logo that represents the look and feel of the company.
• Please incorporate these colours - blue, yellow and white - into the powerpoint template

```html
<!DOCTYPE html>
<html lang="en">
<head>
<meta charset="utf-8">
<title>Channel Spend Clearview — Project Title</title>
<link rel="stylesheet" href="https://fonts.googleapis.com/css2?family=Roboto+Condensed:wght@500;700&display=swap">
<style>
  :root {
    --brand-blue: #1a64ae;
    --brand-yellow: #fbee3e;
    --name-blue: #2a6db3;
    --white: #ffffff;
    --footer-grey: #a6a6a6;
  }
  * { margin: 0; padding: 0; box-sizing: border-box; }
  html, body {
    width: 1200px;
    height: 900px;
    overflow: hidden;
    background: var(--white);
  }
  .slide {
    position: relative;
    width: 1200px;
    height: 900px;
    font-family: "Roboto Condensed", "Arial Narrow", sans-serif;
  }
  .hero {
    position: absolute;
    left: 0; top: 0;
    width: 1200px;
    height: 556px;
    background: var(--brand-blue);
    color: var(--white);
    text-align: center;
  }
  .hero-title {
    position: absolute;
    left: 0; right: 0;
    top: 240px;
    font-weight: 700;
    font-size: 69px;
    line-height: 1;
    letter-spacing: 1px;
  }
  .hero-subtitle {
    position: absolute;
    left: 50%;
    top: 322px;
    width: 790px;
    transform: translateX(-50%);
    font-weight: 500;
    font-size: 24px;
    line-height: 39px;
  }
  .brand {
    position: absolute;
    left: 402px;
    top: 640px;
    display: flex;
    align-items: center;
    gap: 32px;
  }
  .brand-square {
    width: 141px;
    height: 142px;
    background: var(--brand-yellow);
  }
  .brand-name {
    color: var(--name-blue);
    font-weight: 500;
    font-size: 37px;
    line-height: 48px;
  }
  .footer-band {
    position: absolute;
    left: 0; bottom: 0;
    width: 1200px;
    height: 33px;
    background: var(--footer-grey);
  }
</style>
</head>
<body>
  <main class="slide">
    <section class="hero">
      <h1 class="hero-title">PROJECT TITLE HERE</h1>
      <p class="hero-subtitle">Subtext here Subtext here Subtext here Subtext here Subtext here Subtext here Subtext here Subtext here Subtext here Subtext here</p>
    </section>
    <div class="brand">
      <div class="brand-square"></div>
      <div class="brand-name">Channel<br>Spend<br>Clearview</div>
    </div>
    <div class="footer-band"></div>
  </main>
</body>
</html>
```